Scientific Conference A0 Poster

I need an A0 poster for a Emergency Medicine scientific conference designed urgently. Attached is the information needed/specification,
as well as a previous poster. Your creativity is much appreciated. Here is a link to how to create a poster (no doubt things you already know), there are also examples of other posters medical posters. I want mine to be the best.
https://www.vantelquill.co.uk/briefs/how-to-make-a-poster/
Please keep the Holbury and Fenwick Care Trust and HCS logos/graphics
Please can you find a way to graphically represent the visual elements listed in the specification as well as the statistics listed in the specification. The statistics should not just be quoted, they need to be graphically represented, if possible. I am comfortable with whatever you think works.
Target Market(s)
Doctors and Healthcare management
Industry/Entity Type
Healthcare
Look and feel

```html
<!DOCTYPE html>
<html lang="en">
<head>
<meta charset="utf-8">
<title>Crowding in Emergency Departments During COVID-19</title>
<link href="https://fonts.googleapis.com/css2?family=Tinos:ital,wght@0,400;0,700;1,400&display=swap" rel="stylesheet">
<style>
:root{
  --blue:#0a5cbf;
  --title-blue:#1457b8;
  --ink:#1e1e1e;
  --yellow:#f2e600;
  --rule:#c8c8c8;
  --white:#ffffff;
  --navy:#0b1f45;
}
*{margin:0;padding:0;box-sizing:border-box}
html,body{width:927px;height:1200px;overflow:hidden;background:var(--white)}
body{font-family:"Tinos","Times New Roman",serif;color:var(--ink);position:relative}
.hero{position:absolute;left:3px;top:0;width:924px;height:196px;
  background:linear-gradient(90deg,#2f3c5c 0%,#56648a 30%,#a3adc6 55%,#e4e7ef 72%,#ffffff 86%)}
.brand{position:absolute;right:19px;top:25px;display:flex;align-items:center;gap:10px}
.brand-name{font-weight:700;font-size:20px;color:var(--navy)}
.brand-square{width:38px;height:38px;background:var(--blue)}
.title{position:absolute;left:20px;top:90px;width:890px;font-size:34.5px;letter-spacing:-0.2px;font-weight:700;color:var(--title-blue);white-space:nowrap;text-shadow:0 0 2px #fff,0 0 2px #fff}
.subtitle{position:absolute;left:44px;top:136px;font-size:18.5px;color:var(--yellow);white-space:nowrap}
.subtitle-rule{position:absolute;left:726px;top:146px;width:182px;height:6px;background:var(--rule)}
.author{position:absolute;left:43px;top:159px;font-size:18.5px;font-style:italic;color:var(--yellow)}
.divider{position:absolute;left:461px;top:196px;width:4px;height:966px;background:var(--rule)}
.band{position:absolute;height:38px;background:var(--blue);color:var(--white);font-weight:700;font-size:16.5px;display:flex;align-items:center;justify-content:center}
.band.left{left:19px;width:418px}
.band.right{left:489px;width:419px}
.block{position:absolute;text-align:center;font-size:16px;line-height:18.5px;letter-spacing:0.2px}
.block.left{left:22px;width:412px}
.block.right{left:492px;width:413px}
.block b{font-weight:700}
.block h3{font-size:16px;font-weight:700}
.bullet::before{content:"";display:inline-block;width:6px;height:6px;border-radius:50%;background:var(--blue);margin-right:7px;vertical-align:2px}
.chart{position:absolute;left:19px;top:448px;width:415px;height:285px}
.chart text{font-family:"Tinos","Times New Roman",serif;letter-spacing:0}
</style>
</head>
<body>
<div class="hero" role="img" aria-label="Photograph of a busy crowd of people in a hospital waiting area, fading to white"></div>

<div class="brand"><span class="brand-name">Holbury and Fenwick Care Trust</span><span class="brand-square"></span></div>

<h1 class="title">Crowding in Emergency Departments During COVID-19</h1>
<p class="subtitle">A Critical Review of existing and novel measures adopted by global health institutions</p>
<div class="subtitle-rule"></div>
<p class="author">Dr Tomas Elrick, Emergency Medicine Consultant</p>

<div class="divider"></div>

<!-- Left column -->
<div class="block left" style="top:213px">Emergency departments (ED) experienced unprecedented crowding during the COVID-19 pandemic.</div>
<div class="block left" style="top:269px">Hospitals faced increased healthcare demand, leading to overflows in intensive care units and emergency care, with limited hospital bed availability.</div>
<div class="block left" style="top:343px"><h3>Statistical Data</h3>During COVID-19, daily admissions reached an average of 157 per day, with EDs spending 152 days in overcrowding. (Marchetti-Dunn et al., 2021)</div>

<svg class="chart" viewBox="0 0 415 285" role="img" aria-label="Line chart of UK daily new hospital admissions for COVID-19 by nation, 2020 to 2023">
  <text x="8" y="14" font-size="11.5" fill="#555">UK: Daily new hospital admissions for COVID-19</text>
  <rect x="378" y="2" width="32" height="16" fill="#0b2a55"/>
  <text x="8" y="24" font-size="5.6" fill="#777">Hospital data is available for individual UK nations, and English data by region. Figures are not comparable</text>
  <text x="8" y="31" font-size="5.6" fill="#777">between nations as Wales includes suspected COVID-19 patients while the other nations only include confirmed</text>
  <text x="8" y="38" font-size="5.6" fill="#777">cases.</text>
  <g stroke="#e3e3e3" stroke-width="0.6" stroke-dasharray="2 2">
    <line x1="31" y1="70" x2="346" y2="70"/><line x1="31" y1="96" x2="346" y2="96"/>
    <line x1="31" y1="122" x2="346" y2="122"/><line x1="31" y1="149" x2="346" y2="149"/>
    <line x1="31" y1="175" x2="346" y2="175"/><line x1="31" y1="201" x2="346" y2="201"/>
    <line x1="31" y1="228" x2="346" y2="228"/>
  </g>
  <line x1="31" y1="254" x2="346" y2="254" stroke="#bbb" stroke-width="0.6"/>
  <g font-size="6" fill="#777" text-anchor="end">
    <text x="26" y="72">3,500</text><text x="26" y="98">3,000</text><text x="26" y="124">2,500</text>
    <text x="26" y="151">2,000</text><text x="26" y="177">1,500</text><text x="26" y="203">1,000</text>
    <text x="26" y="230">500</text><text x="26" y="256">0</text>
  </g>
  <g transform="translate(-18.54 254) scale(0.618 -0.0526)" fill="none" stroke-linejoin="round">
    <polyline vector-effect="non-scaling-stroke" stroke="#c8561b" stroke-width="1" points="80,1000 86,2700 95,1800 105,900 120,300 140,60 155,100 165,900 170,1500 176,1200 185,2200 191,3750 197,2500 205,900 215,350 230,100 245,150 255,400 262,750 268,800 275,700 285,800 295,700 305,850 315,750 325,2050 333,1500 343,1000 350,1600 358,2100 366,1500 373,800 380,450 388,900 397,1850 405,1300 415,550 422,650 430,1200 437,800 445,500 452,700 458,1150 465,800 472,650 478,900 488,1050 497,750 508,450 520,200 530,100 540,200 550,400 557,350 565,600 572,450 580,300 588,400"/>
    <polyline vector-effect="non-scaling-stroke" stroke="#b8325a" stroke-width="0.8" points="80,80 86,250 95,150 110,60 140,20 170,120 190,250 205,100 230,20 260,90 290,100 320,200 335,120 358,260 375,120 400,200 418,60 430,80"/>
    <polyline vector-effect="non-scaling-stroke" stroke="#2a8a6e" stroke-width="0.8" points="80,20 90,60 120,10 190,60 230,10 330,30 360,40 400,20 420,10"/>
    <polyline vector-effect="non-scaling-stroke" stroke="#6b3e9a" stroke-width="0.8" points="80,40 90,100 120,15 170,40 192,110 215,30 260,40 330,60 360,70 420,10 590,5"/>
  </g>
  <text x="361" y="237" font-size="6" fill="#c8561b">England</text>
  <text x="361" y="248" font-size="6" fill="#b8325a">Scotland</text>
  <text x="361" y="255" font-size="6" fill="#2a8a6e">Northern Ireland</text>
  <text x="361" y="262" font-size="6" fill="#6b3e9a">Wales</text>
  <g font-size="6" fill="#777" text-anchor="middle">
    <text x="46" y="263">Mar 8, 2020</text><text x="112" y="263">Feb 24, 2021</text>
    <text x="159" y="263">Sep 12, 2021</text><text x="198" y="263">Mar 31, 2022</text>
    <text x="248" y="263">Oct 17, 2022</text><text x="326" y="263">Dec 8, 2023</text>
  </g>
  <text x="8" y="278" font-size="5.6" fill="#666"><tspan font-weight="700">Data source:</tspan> National Health Statistics Office (2024)</text>
  <text x="410" y="278" font-size="5.6" fill="#666" text-anchor="end">openhealthcharts.org/respiratory | CC BY</text>
</svg>

<div class="band left" style="top:749px">Addressing ED Crowding</div>
<div class="block left" style="top:813px"><b>Hospital Transformations:</b> Adaptations such as creating dedicated COVID-19 treatment zones and expanding telehealth services.</div>
<div class="block left" style="top:887px"><b>Process Optimisation:</b> Fast-track pathways, improved triage, and discharge planning were implemented to improve patient flow.</div>
<div class="block left" style="top:961px"><b>Leadership &amp; Training:</b> Enhanced adaptability through evidence-based training programs, ensuring efficient ED management during surges.</div>
<div class="block left" style="top:1034px"><h3>Statistical Data</h3><span class="bullet"></span>Each hour of ambulance diversion is associated with $1,086 deducted from hospital revenue (Brennock et al., 2020).<br><span class="bullet"></span>Reducing ambulance diversion could save hospitals around $9,000 annually (Brennock et al., 2020).</div>

<!-- Right column -->
<div class="band right" style="top:181px">The Impact of ED Crowding During COVID-19</div>
<div class="block right" style="top:244px">Overcrowding peaked during the pandemic, with a 28% increase following the removal of COVID-19 lockdowns. (Harlowe et al., 2020)</div>
<div class="block right" style="top:318px">This led to high-risk environments for both patients and staff, resulting in medical errors, prolonged hospital stays, and increased in-hospital mortality.</div>
<div class="block right" style="top:392px"><h3>Statistical Data</h3>25% of patients required urgent hospital admission during the pandemic. (Ferrand et al., 2020)</div>

<div class="band right" style="top:481px">Technological Solutions for Managing ED Crowding</div>
<div class="block right" style="top:544px"><b>Telemedicine:</b> Remote delivery of healthcare services using telecommunication technologies.</div>
<div class="block right" style="top:598px"><b>Internet Hospitals:</b> Implementation of multi-centre internet hospitals to reduce physical ED visits and crowding.</div>
<div class="block right" style="top:654px"><b>AI Advancements:</b> AI-enabled tools like virtual waiting rooms and online symptom checkers streamlined patient management.</div>
<div class="block right" style="top:728px"><h3>Statistical Data</h3><span class="bullet"></span>By the end of 2021, experts expected 1 billion telehealth visits globally (Okafor et al., 2021)</div>

<div class="band right" style="top:818px">Recommendations for Future Crowding Management</div>
<div class="block right" style="top:882px"><b>Data-driven Real-Time Bottleneck removal</b>: Live dashboards pinpoint resource constraints (imaging, labs, beds) and patient acuity for dynamic resource allocation and on-the-fly interventions.</div>
<div class="block right" style="top:975px"><b>Empowered Interdepartmental Collaboration</b>: Interdepartmental visibility and shared ownership of patient flow. Multidisciplinary patient flow teams. Inpatient units proactively prepare for admissions, optimising bed availability.</div>
<div class="block right" style="top:1085px"><b>Proactive Community Care</b>: Leveraging telehealth and community partnerships for remote monitoring, virtual urgent care, and preventative care to reduce ED demand.</div>
</body>
</html>
```